Flyer Design Project

Painting and Maintenance
This is what I have as idea as Job description
Refresh, renew & revive your home. from painting to carpentry. Do you guys have any epic unique slogan?
As what we do Residential - Commercial Interior - ExteriorTrim & Molding installationWainscoting - Wallpaper removalCabinet refinishing Woodwork EnamelingDeck & Fence Cleaning & SealingPressure washConcrete & Paver Washing
I would like to have a note that says-Prompt professional service-Free estimates-Insured -"visit us on ChatHive"
I would like new ideas from you guys as well!
Carpentry

```html
<!DOCTYPE html>
<html lang="en">
<head>
<meta charset="utf-8">
<title>Hartwell Painting &amp; Maintenance – Trifold Brochure</title>
<link rel="stylesheet" href="https://fonts.googleapis.com/css2?family=Oswald:wght@400;500;700&family=Lato:wght@400;700&display=swap">
<style>
  :root{
    --red:#b3181d;
    --black:#0b0b0b;
    --white:#ffffff;
    --ink:#1d1d1d;
    --grey:#3a3a3a;
    --backdrop:#d9d9d9;
    --lawn:#5f8a3a;
    --paver:#a9b4bd;
    --sky:#6aa4df;
    --siding:#c9b34c;
  }
  *{box-sizing:border-box;margin:0;padding:0}
  html,body{width:1200px;height:1200px;overflow:hidden;background:var(--backdrop)}
  .brochure{position:absolute;left:40px;top:233px;width:1120px;height:733px;background:var(--white);box-shadow:0 6px 18px rgba(0,0,0,.25);font-family:"Lato",sans-serif;overflow:hidden}
  .brochure-shapes{position:absolute;inset:0}
  .panel{position:absolute;top:0;height:716px}
  .panel-about{left:0;width:372px}
  .panel-why{left:372px;width:372px}
  .panel-cover{left:744px;width:376px}
  .base-band{position:absolute;left:0;bottom:0;width:100%;height:17px;background:var(--black)}

  .heading{font-family:"Oswald",sans-serif;font-weight:500;color:var(--red);text-transform:uppercase;letter-spacing:-.3px;transform:scaleX(.82);transform-origin:left}
  .about-heading{position:absolute;left:38px;top:388px;font-size:29px}
  .about-text{position:absolute;left:38px;top:434px;width:300px;font-size:14.8px;line-height:19.2px;color:var(--ink);text-align:justify}
  .brand-small{position:absolute;left:0;width:100%;top:634px;text-align:center;font-family:"Lato",sans-serif;font-weight:700;font-size:13px;line-height:14px;color:var(--grey)}
  .site-spaced{position:absolute;width:100%;text-align:center;font-family:"Lato",sans-serif;font-weight:700;font-size:16px;letter-spacing:4.3px;color:var(--ink)}
  .panel-about .site-spaced{top:667px}

  .why-heading{position:absolute;left:36px;top:111px;font-size:23px}
  .why-text{position:absolute;left:35px;top:152px;width:314px;font-size:14.6px;line-height:19.2px;color:var(--white)}
  .why-text p{margin-bottom:19px;text-align:justify}
  .contact-button{position:absolute;left:112px;top:480px;width:141px;height:39px;background:var(--red);color:var(--white);font-family:"Oswald",sans-serif;font-weight:500;font-size:25px;line-height:39px;text-align:center;text-transform:uppercase}
  .contact-button span{display:inline-block;transform:scaleX(.82)}
  .contact-list{position:absolute;left:0;top:528px;width:100%;text-align:center;color:var(--white);font-size:16.5px;line-height:21px}
  .contact-list svg{display:block;margin:0 auto 3px;width:15px;height:15px}
  .contact-item{margin-bottom:7px}

  .brand-large{position:absolute;left:0;top:46px;width:100%;text-align:center;font-family:"Lato",sans-serif;font-weight:700;color:var(--grey);font-size:29px;line-height:32px}
  .brand-large small{display:block;font-size:13px;letter-spacing:1.6px;line-height:20px}
  .tagline-top{position:absolute;left:0;width:100%;top:530px;text-align:center;font-family:"Oswald",sans-serif;font-weight:400;font-size:35px;color:var(--ink);text-transform:uppercase}
  .tagline-main{position:absolute;left:0;width:100%;top:568px;text-align:center;font-family:"Oswald",sans-serif;font-weight:700;font-size:70px;line-height:90px;color:var(--red);text-transform:uppercase}
  .panel-cover .site-spaced{top:666px}
</style>
</head>
<body>
<main class="brochure">
  <svg class="brochure-shapes" viewBox="0 0 1120 733" width="1120" height="733" aria-hidden="false">
    <defs>
      <linearGradient id="paver-fade" x1="0" y1="0" x2="0" y2="1">
        <stop offset="0" stop-color="var(--lawn)"/>
        <stop offset=".3" stop-color="var(--lawn)"/>
        <stop offset=".36" stop-color="var(--paver)"/>
        <stop offset=".75" stop-color="#c4ccd2"/>
        <stop offset="1" stop-color="#ffffff"/>
      </linearGradient>
      <linearGradient id="house-tone" x1="0" y1="0" x2="1" y2="1">
        <stop offset="0" stop-color="var(--sky)"/>
        <stop offset=".45" stop-color="#8e9aa3"/>
        <stop offset="1" stop-color="var(--siding)"/>
      </linearGradient>
    </defs>
    <!-- about panel photo -->
    <rect x="0" y="0" width="372" height="390" fill="url(#paver-fade)" role="img" aria-label="Photo of a painter sealing a paver patio beside a lawn"/>
    <!-- middle panel black -->
    <rect x="372" y="0" width="372" height="716" fill="var(--black)"/>
    <!-- cover panel photo -->
    <polygon points="744,124 957,188 1120,119 1120,444 957,525 744,431" fill="url(#house-tone)" role="img" aria-label="Photo of a freshly painted house gable with yellow siding"/>
    <!-- top white band -->
    <polygon points="372,0 1120,0 1120,119 957,188 744,124" fill="#f2f2f2"/>
    <polyline points="372,0 744,124 957,188 1120,119" fill="none" stroke="var(--red)" stroke-width="7"/>
    <!-- lower chevron band -->
    <polygon points="744,431 957,525 1120,444 1120,462 957,545 744,450" fill="var(--red)"/>
    <polyline points="744,426 957,520 1120,439" fill="none" stroke="var(--white)" stroke-width="3"/>
  </svg>

  <section class="panel panel-about">
    <h2 class="heading about-heading">About us :</h2>
    <p class="about-text">In publishing and graphic design, lorem ipsum is a filler text or greeking commonly used to demonstrate the textual elements of a graphic document or visual .In publishing and graphic design, lorem ipsum is a filler text or greeking commonly used demonstrate the textual elements of a graphic document or visual .In publishing and graphic design,</p>
    <div class="brand-small">Hartwell<br>Painting</div>
    <div class="site-spaced">www.website.com</div>
  </section>

  <section class="panel panel-why">
    <h2 class="heading why-heading">Why you choose us</h2>
    <div class="why-text">
      <p>Lorem Ipsum is also known as: Greeked text, blind text, placeholder text, dummy content, filler text, lipsum, and mock-content.</p>
      <p>Lorem Ipsum is also known as: Greeked text, blind text, placeholder text, dummy content, filler text, lipsum, and mock-content.</p>
      <p>Lorem Ipsum is also known as: Greeked text, blind text, placeholder text, dummy content, filler text, lipsum, and mLorem Ipsum is also known as: Greeked text, blind text, placeholder text, dummy content, filler text, lipsum, and mock-content.ock-content.Lorem Ipsum is also known as: Greeked text, blind text, placeholder text, dummy content.</p>
    </div>
    <div class="contact-button"><span>Contact us</span></div>
    <div class="contact-list">
      <div class="contact-item">
        <svg viewBox="0 0 16 16" aria-hidden="true"><circle cx="8" cy="8" r="7" fill="none" stroke="#fff" stroke-width="1.2"/><path d="M5.5 4.5l1.3 1.6-.8 1c.6 1.2 1.4 2 2.6 2.6l1-.8 1.6 1.3-.9 1.2C7.6 11.2 4.9 8.5 4.6 5.4z" fill="#fff"/></svg>
        49 -104- 20000
      </div>
      <div class="contact-item">
        <svg viewBox="0 0 16 16" aria-hidden="true"><circle cx="8" cy="8" r="6.5" fill="none" stroke="#fff" stroke-width="1.2"/><ellipse cx="8" cy="8" rx="3" ry="6.5" fill="none" stroke="#fff" stroke-width="1"/><path d="M1.5 8h13M2.5 5h11M2.5 11h11" stroke="#fff" stroke-width="1"/></svg>
        www.website.com
      </div>
      <div class="contact-item">
        <svg viewBox="0 0 16 16" aria-hidden="true"><path d="M8 15S3 9.5 3 6a5 5 0 0 1 10 0c0 3.5-5 9-5 9z" fill="none" stroke="#fff" stroke-width="1.2"/><circle cx="8" cy="6" r="1.8" fill="none" stroke="#fff" stroke-width="1.1"/></svg>
        in publishing and graphic design,<br>lorem ipsum
      </div>
    </div>
  </section>

  <section class="panel panel-cover">
    <div class="brand-large">Hartwell<br>Painting<small>&amp; MAINTENANCE LLC.</small></div>
    <div class="tagline-top">Your world</div>
    <div class="tagline-main">In color</div>
    <div class="site-spaced">www.website.com</div>
  </section>

  <div class="base-band"></div>
</main>
</body>
</html>
```